Business cards and stationery for new company logo
TRV Enterprises
Business cards and stationery for new company logo - Construction
Creative Brief
Simple
Marcus Pellham
Owner
742 Wildrow Ave. Brennick, Eastvale K4T 2B5
marcus@trventerprises.ca
www.trventerprises.ca
Would like something sleek and corporate looking. Catchy. The logo that was designed has all those elements...I would like the bus cards and stationery to also have those.

```html
<!DOCTYPE html>
<html lang="en">
<head>
<meta charset="utf-8">
<title>TRV Enterprises – Business Cards</title>
<link rel="stylesheet" href="https://fonts.googleapis.com/css2?family=Michroma&display=swap">
<style>
  :root {
    --bg: #d6d6d6;
    --ink: #231f20;
    --paper: #ffffff;
    --red: #e0201b;
    --grey: #6d6d6d;
    --light: #f2f2f2;
  }
  * { margin: 0; padding: 0; box-sizing: border-box; }
  html, body { width: 1200px; height: 987px; overflow: hidden; }
  body {
    background: var(--bg);
    font-family: "Michroma", "Arial", sans-serif;
    position: relative;
  }
  .card {
    position: absolute;
    width: 760px;
    height: 434px;
    border-radius: 26px;
    overflow: hidden;
    box-shadow: 0 14px 30px rgba(0,0,0,0.22);
  }
  .card-back {
    left: 260px;
    top: 44px;
    background: var(--ink);
    color: var(--paper);
  }
  .card-back .brand {
    position: absolute;
    left: 0; right: 0;
    top: 170px;
    text-align: center;
    font-size: 46px;
    letter-spacing: 2px;
    color: var(--paper);
  }
  .card-back .web {
    position: absolute;
    left: 0; right: 0;
    top: 258px;
    text-align: center;
    font-size: 13px;
    letter-spacing: 6px;
    text-transform: uppercase;
    color: var(--paper);
  }
  .card-front {
    left: 180px;
    top: 510px;
    background: var(--paper);
  }
  .card-front .shapes {
    position: absolute;
    inset: 0;
    width: 100%;
    height: 100%;
  }
  .card-front .brand {
    position: absolute;
    left: 52px;
    top: 78px;
    font-size: 38px;
    letter-spacing: 1px;
    color: var(--ink);
  }
  .contact {
    position: absolute;
    left: 52px;
    top: 170px;
    list-style: none;
    font-size: 12px;
    letter-spacing: 1.5px;
    color: var(--grey);
    text-transform: uppercase;
  }
  .contact li {
    display: flex;
    align-items: center;
    height: 24px;
  }
  .contact .icon {
    width: 14px;
    height: 14px;
    margin-right: 10px;
    flex: none;
  }
  .contact .indent { padding-left: 24px; }
  .person {
    position: absolute;
    right: 48px;
    bottom: 40px;
    text-align: right;
  }
  .person .name {
    font-size: 15px;
    letter-spacing: 2px;
    color: var(--red);
    text-transform: uppercase;
  }
  .person .role {
    margin-top: 6px;
    font-size: 11px;
    letter-spacing: 2px;
    color: var(--grey);
    text-transform: uppercase;
  }
</style>
</head>
<body>

<section class="card card-back">
  <div class="brand">TRV Enterprises</div>
  <div class="web">www.trventerprises.ca</div>
</section>

<section class="card card-front">
  <svg class="shapes" viewBox="0 0 760 434" preserveAspectRatio="none" aria-hidden="true">
    <path d="M0 70 C160 10 380 -6 620 30 C430 14 220 30 0 92 Z" fill="var(--red)"/>
    <path d="M506 0 C548 180 640 286 760 342 L760 0 Z" fill="var(--light)"/>
    <path d="M760 0 L760 330 C650 270 560 170 520 0 Z" fill="var(--ink)"/>
  </svg>

  <div class="brand">TRV Enterprises</div>

  <ul class="contact">
    <li>
      <svg class="icon" viewBox="0 0 14 14"><path d="M7 1 C4.2 1 2.5 3 2.5 5.3 C2.5 8.4 7 13 7 13 C7 13 11.5 8.4 11.5 5.3 C11.5 3 9.8 1 7 1 Z" fill="var(--red)"/><circle cx="7" cy="5.3" r="1.8" fill="var(--paper)"/></svg>
      742 Wildrow Ave.
    </li>
    <li class="indent">Brennick, Eastvale</li>
    <li class="indent">K4T 2B5</li>
    <li>
      <svg class="icon" viewBox="0 0 14 14"><circle cx="7" cy="7" r="7" fill="var(--red)"/><path d="M4.6 3.6 L6 5.6 L5.2 6.4 C5.7 7.5 6.5 8.3 7.6 8.8 L8.4 8 L10.4 9.4 L9.6 10.6 C6.8 10.4 3.6 7.2 3.4 4.4 Z" fill="var(--paper)"/></svg>
      T 555 010 4417
    </li>
    <li>
      <svg class="icon" viewBox="0 0 14 14"><circle cx="7" cy="7" r="7" fill="var(--red)"/><rect x="3.5" y="4.5" width="7" height="5" fill="var(--paper)"/><path d="M3.5 4.5 L7 7.3 L10.5 4.5" stroke="var(--red)" stroke-width="0.9" fill="none"/></svg>
      marcus@trventerprises.ca
    </li>
    <li>
      <svg class="icon" viewBox="0 0 14 14"><circle cx="7" cy="7" r="7" fill="var(--red)"/><circle cx="7" cy="7" r="3.8" stroke="var(--paper)" stroke-width="1" fill="none"/><path d="M3.2 7 H10.8 M7 3.2 V10.8" stroke="var(--paper)" stroke-width="0.9"/></svg>
      www.trventerprises.ca
    </li>
  </ul>

  <div class="person">
    <div class="name">Marcus Pellham</div>
    <div class="role">Owner</div>
  </div>
</section>

</body>
</html>
```